Web Design Project

Psychotherapist in Private Practice
Practice name "The Steady Harbor"
The population is professional adults seeking life coaching and change consultation
I am including a photo for inspiration ONLY - It includes the theme of light and tree branches. There does not HAVE to be a photograph . An illustration , concept or theme of nature /light / generativity / growth / creativity is acceptable
Clean sharp lines Light colors, minimalist , modern.
There is a separate project for a logo design that will become part of the web design
Here are examples of two logos/websites I like
http://www.quietrivergroup.example/
http://www.brightknollpartners.example/

Target Market(s)

Professional adults seeking life coaching

Industry/Entity Type

Life Coaching

Requirements
Should not have
• Although the business name has 'compassion' in it, designs with hearts in it would have to be pretty stylish, subtle, mature and sophisticated to be considered.

```html
<!DOCTYPE html>
<html lang="en">
<head>
<meta charset="utf-8">
<title>The Steady Harbor</title>
<link href="https://fonts.googleapis.com/css2?family=Open+Sans:wght@400;600;700&family=Arimo:wght@400;700&display=swap" rel="stylesheet">
<style>
:root{
  --blue:#1a8fd1;
  --blue-dark:#0a5fa8;
  --green:#2fbf4a;
  --ink:#333;
  --muted:#555;
  --line:#d6d6d6;
  --panel:#f4f4f4;
  --footer:#262626;
  --footer-text:#e6e6e6;
}
*{box-sizing:border-box;margin:0;padding:0}
html,body{width:1067px;height:1200px;overflow:hidden;background:#fff}
body{position:relative;font-family:'Open Sans',sans-serif;color:var(--ink)}
.abs{position:absolute}
.site-header{left:0;top:0;width:1067px;height:105px;background:linear-gradient(#fff,#e8e8e8);border-bottom:1px solid #d0d0d0}
.brand{left:91px;top:30px;font-size:28px;font-weight:700;color:var(--blue);display:flex;align-items:center;gap:10px}
.brand-dot{width:12px;height:12px;border-radius:50%;background:var(--green)}
.social{top:11px;display:flex;gap:9px;left:873px}
.social span{width:25px;height:25px;border-radius:4px;background:linear-gradient(#f2f2f2,#c9c9c9);border:1px solid #b8b8b8}
.phone{left:709px;top:40px;display:flex;align-items:center;gap:8px;font-size:25px;color:#333}
.phone .area{color:var(--blue)}
.phone-icon{width:32px;height:32px;border-radius:50%;background:linear-gradient(#f4f4f4,#d2d2d2);border:1px solid #c4c4c4;display:flex;align-items:center;justify-content:center}
.email{left:754px;top:70px;font-size:14.5px;color:var(--blue);text-decoration:underline}
.intro h1{font-weight:400;font-size:27px;line-height:34px;color:#333}
.intro{left:91px;top:137px;width:318px}
.intro .rule{margin-top:8px;height:1px;background:var(--line);position:relative}
.intro .rule::before{content:"";position:absolute;left:0;top:-2px;width:134px;height:4px;background:#ccc}
.intro p{font-family:Arimo,sans-serif;font-size:11px;line-height:17.8px;color:#222;text-align:justify;margin-top:18px}
.btn-help{left:92px;top:390px;width:152px;height:37px;border-radius:4px;background:linear-gradient(#2a86d4,#0a5ba6);color:#fff;font-weight:700;font-size:19px;display:flex;align-items:center;justify-content:center;letter-spacing:.5px}
.hero{left:429px;top:134px;width:548px;height:309px;border:5px solid #e4e4e4;background:#ddd}
.hero-photo{width:100%;height:100%;background:linear-gradient(#d89a2a 0%,#f5c845 35%,#fff3b0 55%,#d98a2a 62%,#6a3c2a 78%,#3a2a2a 100%)}
.hero-caption{left:0;bottom:0;width:100%;height:63px;background:rgba(40,40,40,.82);color:#fff;padding:4px 12px}
.hero-caption h2{font-weight:400;font-size:24px;line-height:30px}
.hero-caption p{font-family:Arimo,sans-serif;font-size:14px;padding-left:3px}
.hero-shadow{left:440px;top:444px;width:530px;height:20px;background:radial-gradient(ellipse at top,rgba(0,0,0,.18),transparent 70%)}
.tab{top:490px;height:37px;border-radius:4px 4px 0 0;font-size:17.5px;padding:7px 10px;border:1px solid #ccc;border-bottom:none}
.tab-active{left:96px;width:200px;background:linear-gradient(#2b97e0,#0d6fbd);color:#fff;border-color:#0d6fbd}
.tab-idle{left:303px;width:269px;background:linear-gradient(#fafafa,#e2e2e2);color:#222}
.panel{left:96px;top:526px;width:590px;height:225px;border:1px solid #cfcfcf;border-radius:0 4px 4px 4px;background:linear-gradient(#fdfdfd,#f0f0f0)}
.panel-photo{left:10px;top:14px;width:176px;height:120px;border:4px solid #fff;box-shadow:0 0 0 1px #ccc;background:linear-gradient(135deg,#cfd6dc,#f1f3f5 50%,#c9b09a)}
.badge{left:201px;top:14px;width:28px;height:28px;border-radius:3px;background:#1d5fa1;color:#fff;font-size:11px;font-weight:700;display:flex;align-items:center;justify-content:center}
.post-title{left:239px;top:13px;font-size:14px;color:var(--blue)}
.post-date{left:239px;top:31px;font-size:9.5px;color:var(--green)}
.post-text{font-family:Arimo,sans-serif;font-size:10.5px;line-height:16px;color:#222}
.post-lead{left:199px;top:54px;width:382px}
.post-more{left:11px;top:144px;width:570px}
.read-more{left:513px;top:193px;width:66px;height:19px;border-radius:4px;background:var(--blue-dark);color:#fff;font-size:11px;display:flex;align-items:center;justify-content:center}
.feed{left:704px;top:490px;width:260px;height:260px;border:1px solid #aab5cc;background:#fff;font-family:Arimo,sans-serif}
.feed-head{height:29px;background:#3b5a9a;color:#fff;display:flex;justify-content:space-between;align-items:center;padding:0 6px}
.feed-head b{font-family:'Open Sans',sans-serif;font-size:17px}
.feed-head span{font-size:11px}
.feed-item{position:absolute;left:8px;display:flex;gap:8px;font-size:8.5px;color:#333;line-height:13px}
.avatar{width:40px;height:40px;background:linear-gradient(#d8d8d8,#9a9a9a);flex:none}
.feed-name{color:#3b5a9a;font-weight:700;font-size:9px}
.like{display:inline-block;border:1px solid #ccc;background:#f2f2f2;padding:0 5px;color:#888;margin-right:4px}
.scroll{left:246px;top:92px;width:11px;height:90px;background:#f0f0f0;border-left:1px solid #ddd}
.feed-count{left:8px;top:183px;font-size:8px}
.feed-faces{left:8px;top:199px;display:flex;gap:3px}
.feed-faces span{width:37px;height:37px}
.feed-foot{left:8px;top:245px;font-size:7px;color:#666}
.carousel-arrow{top:836px}
.card{top:801px;width:201px}
.card-photo{height:98px;border-radius:3px;border:1px solid #e2e2e2}
.card h3{font-weight:400;font-size:16px;margin-top:10px;color:#333}
.card h3 b{font-weight:600}
.card.alt h3{color:var(--blue)}
.card p{font-size:11px;line-height:20px;color:#555;margin-top:3px;padding-left:2px;white-space:nowrap}
.strip-shadow{left:80px;top:975px;width:907px;height:15px;background:radial-gradient(ellipse at top,rgba(0,0,0,.06),transparent 70%)}
.site-footer{left:0;top:1028px;width:1067px;height:172px;background:repeating-linear-gradient(45deg,#2a2a2a 0 2px,#222 2px 4px);border-top:4px solid var(--blue);color:var(--footer-text)}
.foot-col{top:24px}
.foot-col h4{font-weight:400;font-size:15px;color:#eee;margin-bottom:8px}
.foot-col li{list-style:none;font-size:11.5px;line-height:17.7px}
.foot-divider{top:52px;width:1px;height:112px;background:#555}
.foot-brand{left:780px;top:54px;font-size:19px;font-weight:700;color:#ddd;display:flex;align-items:center;gap:8px}
.foot-brand i{width:28px;height:28px;border-radius:50%;border:2px solid #888}
.foot-copy{left:780px;top:102px;font-size:10.5px;line-height:14px;color:#fff}
</style>
</head>
<body>
<header class="site-header abs">
  <div class="brand abs">The Steady Harbor<span class="brand-dot"></span></div>
  <div class="social abs" aria-label="Social links"><span></span><span></span><span></span></div>
  <div class="phone abs">
    <span class="phone-icon"><svg width="16" height="16" viewBox="0 0 24 24"><path d="M6.6 10.8a15 15 0 0 0 6.6 6.6l2.2-2.2c.3-.3.7-.4 1-.2 1.1.4 2.3.6 3.6.6.6 0 1 .4 1 1V20c0 .6-.4 1-1 1A17 17 0 0 1 3 4c0-.6.4-1 1-1h3.5c.6 0 1 .4 1 1 0 1.3.2 2.5.6 3.6.1.3 0 .7-.2 1z" fill="#666"/></svg></span>
    <span><span class="area">(555)</span> 018 2640</span>
  </div>
  <div class="email abs">hello@steadyharbor.example</div>
</header>

<section class="intro abs">
  <h1>Acquisitions of Private Businesses</h1>
  <div class="rule"></div>
  <p>For family-owned or privately-held businesses, acquisitions transactions offer opportunities for market expansion, growth or streamlining of the business. We can help you develop an acquisition strategy, identify target organizations and strategic partners, determine the appropriate bid price,</p>
  <p>Perform financial and tax due diligence reviews, perform a risk assessment, assess the timing of the sale...</p>
</section>
<div class="btn-help abs">We Can Help.</div>

<section class="hero abs">
  <div class="hero-photo" role="img" aria-label="Sunset over the sea framed by dark tree branches"></div>
  <div class="hero-caption abs">
    <h2>We also offer time-limited effective</h2>
    <p>we can help you develop an acquisition strategy, identify organizations</p>
  </div>
</section>
<div class="hero-shadow abs"></div>

<div class="tab tab-active abs">Health Care Services</div>
<div class="tab tab-idle abs">About Steady Harbor</div>
<section class="panel abs">
  <div class="panel-photo abs" role="img" aria-label="Doctor consulting with a patient at a desk"></div>
  <div class="badge abs">PG</div>
  <div class="post-title abs">Featured Auction Fader</div>
  <div class="post-date abs">May 15, 2012</div>
  <p class="post-text post-lead abs">Lorem Ipsum is simply dummy text of the printing and typesetting industry. Lorem Ipsum has been the industry's standard dummy text ever since the 1500s, when an unknown printer took a galley of type and scrambled it to make a type specimen book. It has survived not only five centuries, but also the leap into electronic typesetting.</p>
  <p class="post-text post-more abs">consultation services for executives, professionals, and individuals coping with personal, marital or family problems, work stress, conflicts, and depression that make it difficult to be productive or feel you are working at your</p>
  <div class="read-more abs">read more</div>
</section>

<aside class="feed abs">
  <div class="feed-head"><b>Community</b><span>Find us on Community</span></div>
  <div class="feed-item" style="top:37px"><div class="avatar" role="img" aria-label="Member avatar"></div><div><div class="feed-name">Dana Reyes</div><div style="margin-top:4px"><span class="like">✓ Like</span>You like this.</div></div></div>
  <div class="feed-item" style="top:92px;width:230px"><div class="avatar" role="img" aria-label="Member avatar"></div><div><div class="feed-name">Dana Reyes</div>I think all of Mexico should throw a party for my birthday this year. Does May 5th work for you?<div style="color:#999;margin-top:3px">18 hours ago</div></div></div>
  <div class="scroll abs"></div>
  <div class="feed-count abs">You and 14,596 others like <span style="color:#3b5a9a">Dana Reyes</span>.</div>
  <div class="feed-faces abs" role="img" aria-label="Thumbnails of followers">
    <span style="background:#b89a6a"></span><span style="background:#7a8ab0"></span><span style="background:#9a8a70"></span><span style="background:#a0a0a0"></span><span style="background:#8a5a50"></span><span style="background:#d0d8e0"></span>
  </div>
  <div class="feed-foot abs">Community social plugin</div>
</aside>

<svg class="carousel-arrow abs" style="left:84px" width="16" height="32" viewBox="0 0 16 32"><path d="M14 2 3 16l11 14" fill="none" stroke="#aaa" stroke-width="2"/></svg>
<svg class="carousel-arrow abs" style="left:967px" width="16" height="32" viewBox="0 0 16 32"><path d="M2 2l11 14L2 30" fill="none" stroke="#aaa" stroke-width="2"/></svg>

<article class="card abs" style="left:111px">
  <div class="card-photo" role="img" aria-label="Nurse talking with a young patient" style="background:linear-gradient(90deg,#e9e6e2,#d7b9a4 50%,#8a4a4a)"></div>
  <h3>What To <b>Expect</b></h3>
  <p>Nunc tempus felis vitae urna. Vivam<br>us porttitor purus nisi eleifend</p>
</article>
<article class="card alt abs" style="left:325px">
  <div class="card-photo" role="img" aria-label="Group of smiling medical staff" style="background:linear-gradient(90deg,#dfe9f0,#9fc2dc 50%,#f0f2f4)"></div>
  <h3>About <b>Coaching</b></h3>
  <p>Nunc tempus felis vitae urna. Vi porti-<br>tor purus nisi eleifend</p>
</article>
<article class="card abs" style="left:540px">
  <div class="card-photo" role="img" aria-label="Surgeon in cap and mask" style="background:linear-gradient(90deg,#bfe2ec,#6fb8d2 55%,#2a6a90)"></div>
  <h3>Surgery Center</h3>
  <p>Nunc tempus felis vitae urna. Viva-<br>mus porttitor purus nisi eleifend</p>
</article>
<article class="card abs" style="left:754px">
  <div class="card-photo" role="img" aria-label="Eye examination with optical equipment" style="background:linear-gradient(90deg,#d9d9d9,#f0eeec 45%,#8a6a5a)"></div>
  <h3>Consultation</h3>
  <p>Nunc tempus felis vitae urna. Vivamus<br>porttitor purus nisi eleifend</p>
</article>
<div class="strip-shadow abs"></div>

<footer class="site-footer abs">
  <nav class="foot-col abs" style="left:101px;top:28px"><h4>Main Navigation</h4><ul><li>Home</li><li>Search Entry</li><li>If Entry</li><li>Video Room</li><li>Plug</li><li>For Business</li></ul></nav>
  <div class="foot-divider abs" style="left:268px;top:46px"></div>
  <nav class="foot-col abs" style="left:332px"><h4>Main Navigation</h4><ul><li>Home</li><li>Search Entry</li><li>If Entry</li><li>Video Room</li><li>Plug</li><li>For Business</li></ul></nav>
  <div class="foot-divider abs" style="left:508px;top:36px"></div>
  <nav class="foot-col abs" style="left:580px"><h4>Main Navigation</h4><ul><li>Home</li><li>Search Entry</li><li>If Entry</li><li>Video Room</li><li>Plug</li><li>For Business</li></ul></nav>
  <div class="foot-divider abs" style="left:747px;top:36px"></div>
  <div class="foot-brand abs"><i></i>Harborline Studio</div>
  <div class="foot-copy abs">Copyright © 2002-2013 Harborline Studio<br>&nbsp;studio@harborline.example</div>
</footer>
</body>
</html>
```